VERUSO - PIZZA - RESTAURANT PIZZERIA

Flyer format:
- A5 front / back leaflet (Example attachment)
Customer logos:
- Attachment, VERUSO PIZZA logo
Address and contact to put on the flyers:
- Phone to add: (+352) 26 58 07 31 (Page 1)
- Address to be added: 8 rue des tilleuls, L-3592 Kayl, Luxembourg (Page 1)
- Website: www.veruso-example.lu (Page 1)
- Leave a space for the timetable (last page)
Flyer color:
- Preferably black background with colored customer logo
Typefaces:
- At your convenience
Descriptions:
- We would like to have a flyer to the one we have put as an example in the attachment
Important elements:
- Pizza oven on the cover page with customer logo, address and contact details
- The graphic elements must be usable and non-paying, we want a quality visual.
- Menu (attachment) The menu is in Word format, it must be laid out in a thoughtful way as on the example model.
- We need to find some pizza and/or ingredient visuals
Aspects :
- The design of the set must be elegant, sober and must contain all the information (Menu, visual of your choice, logo)

Target Market(s)

Private and professional public

Font styles to use
Serif
Sans Serif

Requirements
Must have
• Elegance, take into account the information of the comment
Nice to have
• Pizza oven, Dominant color black, Gold, red
Should not have
• poor quality visuals

```html
<!DOCTYPE html>
<html lang="fr">
<head>
<meta charset="utf-8">
<title>Veruso Pizza – Menu</title>
<link href="https://fonts.googleapis.com/css2?family=Great+Vibes&family=Montserrat:wght@400;500;600;700&display=swap" rel="stylesheet">
<style>
:root{
  --black:#000;
  --tab:#0c0c0c;
  --red:#d40000;
  --gold:#e5b13a;
  --white:#fff;
  --row:19.6px;
}
*{margin:0;padding:0;box-sizing:border-box}
html,body{width:1200px;height:898px;overflow:hidden;background:var(--black)}
body{font-family:"Montserrat",Arial,sans-serif;color:var(--white)}
.flyer{position:relative;width:1200px;height:898px}
.page{position:absolute;top:0;width:600px;height:898px;overflow:hidden;background:var(--black)}
.page-front{left:0}
.page-back{left:600px}
.deco{position:absolute;left:0;top:0;width:600px;height:898px}
.abs{position:absolute}

.hero-photo{position:absolute;left:0;top:0;width:600px;height:330px;
  background:
    radial-gradient(ellipse 140px 90px at 140px 60px,rgba(240,150,40,.55),transparent 70%),
    radial-gradient(ellipse 260px 90px at 300px 230px,rgba(200,120,60,.55),transparent 70%),
    radial-gradient(ellipse 120px 80px at 40px 150px,rgba(120,50,20,.6),transparent 70%),
    linear-gradient(160deg,#3b1f10 0%,#2a1509 40%,#3d2414 70%,#1a0d06 100%);}
.food-bg{position:absolute;border-radius:50%;
  background:radial-gradient(circle,rgba(90,40,25,.35) 0%,rgba(60,25,15,.22) 55%,transparent 72%)}

.brand{position:absolute;left:196px;top:108px;width:180px;text-align:center;color:var(--gold);font-weight:600;line-height:1}
.brand-name{display:block;font-size:38px;letter-spacing:2px}
.brand-sub{display:block;font-size:13px;letter-spacing:10px;margin-top:8px;padding-left:10px}

.script{font-family:"Great Vibes",cursive;color:var(--gold);font-weight:400}
.tab-title{position:absolute;display:flex;align-items:baseline;gap:6px;white-space:nowrap}
.tab-title .script{font-size:36px}
.tab-title .bold{font-weight:700;font-size:18.5px;color:var(--gold)}

.pannini-title{position:absolute;left:346px;top:616px;width:190px;height:56px}
.pannini-title .script{position:absolute;left:0;top:0;font-size:36px;line-height:1.2;white-space:nowrap}
.pannini-title .bold{position:absolute;right:0;top:18px;font-weight:700;font-size:17px;line-height:15px;color:var(--gold);text-align:right;white-space:nowrap}

.menu{position:absolute;list-style:none}
.menu li{display:grid;grid-template-columns:1fr var(--pc,36px);align-items:center;height:var(--row);white-space:nowrap;font-size:10.8px;line-height:1.2}
.menu .name{font-weight:600;font-size:10.8px}
.menu .desc{font-weight:500;font-size:6.7px;letter-spacing:-.05px;margin-left:3px}
.menu .price{font-weight:600;font-size:10.8px}
.menu li.two-line{height:28.8px;align-items:start;padding-top:2px}
.menu li.two-line .sub{display:block;font-weight:500;font-size:6.7px;line-height:9px}
.menu li.two-line .price{line-height:13px}

.contact{position:absolute;left:16px;color:var(--gold);font-weight:700;font-size:18px;line-height:1}
.address{position:absolute;left:331px;top:863px;color:var(--gold);font-weight:600;font-size:11.4px}

.label{position:absolute;font-size:26px;line-height:1}
.section-title{position:absolute;font-size:38px;line-height:1}
.desserts p{height:var(--row);display:flex;align-items:center;font-weight:600;font-size:10.8px;white-space:nowrap}
.desserts .price{margin-left:16px}
.drinks{position:absolute;left:306px;font-size:11px;line-height:13.5px;font-weight:400}
.drink-head{position:absolute;left:306px;display:flex;align-items:baseline;gap:10px;white-space:nowrap}
.drink-head .script{font-size:24px}
.drink-head .bold{font-weight:700;font-size:12.5px}
.programme-title{position:absolute;left:366px;top:726px;font-size:40px}
</style>
</head>
<body>
<main class="flyer">

  <!-- FRONT PAGE -->
  <section class="page page-front">
    <div class="hero-photo" role="img" aria-label="Photo of a pizza in front of a wood-fired oven with flames"></div>
    <div class="food-bg" style="left:250px;top:380px;width:520px;height:520px" role="img" aria-label="Faint background photo of a pizza"></div>

    <svg class="deco" viewBox="0 0 600 898" aria-hidden="true">
      <path d="M0,314 C70,266 150,250 240,262 C360,278 470,306 600,310 L600,898 L0,898 Z" fill="#000"/>
      <path d="M0,312 C70,264 150,248 240,260 C360,276 470,304 600,308" fill="none" stroke="var(--red)" stroke-width="5"/>
      <path d="M62,336 H245 Q264,336 264,360 V392 H62 Z" fill="var(--tab)"/>
      <path d="M0,344 H62" stroke="var(--red)" stroke-width="5"/>
      <path d="M62,336 H245 Q264,336 264,362" fill="none" stroke="var(--red)" stroke-width="5"/>
      <path d="M540,336 H356 Q336,336 336,360 V392 H540 Z" fill="var(--tab)"/>
      <path d="M540,344 H600" stroke="var(--red)" stroke-width="5"/>
      <path d="M540,336 H356 Q336,336 336,362" fill="none" stroke="var(--red)" stroke-width="5"/>
      <path d="M540,618 H356 Q336,618 336,642 V675 H540 Z" fill="var(--tab)"/>
      <path d="M540,627 H600" stroke="var(--red)" stroke-width="5"/>
      <path d="M540,618 H356 Q336,618 336,644" fill="none" stroke="var(--red)" stroke-width="5"/>
    </svg>

    <div class="brand"><span class="brand-name">VERUSO</span><span class="brand-sub">PIZZA</span></div>

    <h2 class="tab-title" style="left:66px;top:340px"><span class="script">Pizza</span><span class="bold">Base tomate</span></h2>
    <h2 class="tab-title" style="left:358px;top:342px"><span class="script">Pizza</span><span class="bold">Base crème</span></h2>
    <h2 class="pannini-title"><span class="script">Pannini</span><span class="bold">Base crème<br>+ mozza</span></h2>

    <ul class="menu" style="left:16px;top:393px;width:271px">
      <li><span><span class="name">Marinara</span><span class="desc">anchois,capres,olive,ail</span></span><span class="price">15€</span></li>
      <li><span><span class="name">Napolitaine</span><span class="desc">ail origan</span></span><span class="price">9,50€</span></li>
      <li><span><span class="name">Margharita</span><span class="desc">mozza</span></span><span class="price">10€</span></li>
      <li><span><span class="name">4 fromages</span><span class="desc">mozza,chevre,parmesan,gorgonzola</span></span><span class="price">14,50€</span></li>
      <li><span><span class="name">Chevre</span><span class="desc">mozza,jambon cuit, chevre,olive</span></span><span class="price">15€</span></li>
      <li><span><span class="name">Chorizo</span><span class="desc">mozza, chorizo,poivrons,olive</span></span><span class="price">15€</span></li>
      <li><span><span class="name">Vegetarienne</span><span class="desc">mozza,courgette,olive,poivrons,aubergine</span></span><span class="price">15€</span></li>
      <li><span><span class="name">3viandes</span><span class="desc">mozza,vianche haché, merguez,poulet,poivrons,oeuf</span></span><span class="price">7,50€</span></li>
      <li><span><span class="name">Buffala</span><span class="desc">mozza,buffala</span></span><span class="price">15€</span></li>
      <li><span><span class="name">Calzone jambon</span><span class="desc">mozza,jambon cuit ,champignon,</span></span><span class="price">14,50€</span></li>
      <li><span><span class="name">Calzone chorizo</span><span class="desc">mozza,chorizo,riccota</span></span><span class="price">14,50€</span></li>
      <li><span><span class="name">Bambino</span><span class="desc">mozza,jambon,olive</span></span><span class="price">13€</span></li>
      <li><span><span class="name">Reine</span><span class="desc">mozza, jambon,champignon</span></span><span class="price">14€</span></li>
      <li><span><span class="name">Neptune</span><span class="desc">mozza,thon,oignon,olive</span></span><span class="price">14,50€</span></li>
      <li><span><span class="name">Poulet</span><span class="desc">mozza,poulet,poivron,oignon,champignon,olive</span></span><span class="price">17€</span></li>
      <li><span><span class="name">Campagnarde</span><span class="desc">mozza,jambon,artichaud,champignon,oeuf</span></span><span class="price">15€</span></li>
      <li><span><span class="name">Mediterranienne</span><span class="desc">mozza,fruits de mer</span></span><span class="price">17,50€</span></li>
      <li><span><span class="name">Exotique</span><span class="desc">mozza,poulet,chevre,ananas</span></span><span class="price">16,50€</span></li>
      <li><span><span class="name">4 saisons</span><span class="desc">mozza,champignon,artichaud,jambon cuits, olive</span></span><span class="price">14,50€</span></li>
      <li><span><span class="name">Scampi</span><span class="desc">mozza, ail, origan, scampi</span></span><span class="price">14,50€</span></li>
      <li><span><span class="name">Veruso</span><span class="desc">mozza, porcini,chorizo,mozza fumé</span></span><span class="price">18€</span></li>
    </ul>

    <ul class="menu" style="left:317px;top:393px;width:282px;--pc:40px">
      <li><span><span class="name">Bianca</span><span class="desc">mozza,jambon</span></span><span class="price">12€</span></li>
      <li><span><span class="name">chèvre miel</span><span class="desc">mozza chevre frais miel</span></span><span class="price">13€</span></li>
      <li><span><span class="name">Umberto</span><span class="desc">creme gorgonzola parmesan mozza st nectaire</span></span><span class="price">14,50€</span></li>
      <li><span><span class="name">Fermiere</span><span class="desc">mozza,poulet,champignon,oignon</span></span><span class="price">16€</span></li>
      <li><span><span class="name">Gorgonzola</span><span class="desc">mozza,lardon,oignon,gorgonzola,st nectaire,chevre</span></span><span class="price">16,50€</span></li>
      <li><span><span class="name">Moselle</span><span class="desc">mozza,viande hachée,lardon,pomme de terre</span></span><span class="price">16,50€</span></li>
      <li><span><span class="name">Bauca neve</span><span class="desc">mozza,burrata,andouillette</span></span><span class="price">15,50€</span></li>
      <li class="two-line"><span><span class="name">raquette</span><span class="desc">mozza,riccota,jambon cuit</span><span class="sub">jambon cru,tomate cerise,parmesan</span></span><span class="price">20,50€</span></li>
      <li><span><span class="name">Mortadela</span><span class="desc">mozza burrata,pistache</span></span><span class="price">14,50€</span></li>
      <li class="two-line"><span><span class="name">Parma</span><span class="desc">mozza,tomate cerise,roquette,</span><span class="sub">parmesan,jambon de parme</span></span><span class="price" style="padding-top:5px">17€</span></li>
    </ul>

    <ul class="menu" style="left:317px;top:695px;width:266px;--pc:24px">
      <li><span class="name">4fromages</span><span class="price">7€</span></li>
      <li><span class="name">saumon</span><span class="price">7€</span></li>
      <li><span class="name">merguez</span><span class="price">7€</span></li>
      <li><span class="name">poulet</span><span class="price">7€</span></li>
      <li><span class="name">jambon</span><span class="price">7€</span></li>
      <li><span class="name">viande hachée</span><span class="price">7€</span></li>
    </ul>

    <p class="contact" style="top:831px">(+352) 26 58 07 31</p>
    <p class="contact" style="top:858px">www.veruso-example.lu</p>
    <p class="address">8 rue des tilleuls, L-3592 Kayl, Luxemburgo</p>
  </section>

  <!-- BACK PAGE -->
  <section class="page page-back">
    <div class="food-bg" style="left:380px;top:370px;width:380px;height:380px" role="img" aria-label="Faint background photo of a pizza with toppings"></div>

    <svg class="deco" viewBox="0 0 600 898" aria-hidden="true">
      <defs>
        <linearGradient id="goldFade" x1="0" y1="0" x2="0" y2="1">
          <stop offset="0" stop-color="#e5b13a"/>
          <stop offset=".55" stop-color="#e5b13a" stop-opacity=".6"/>
          <stop offset="1" stop-color="#e5b13a" stop-opacity="0"/>
        </linearGradient>
      </defs>
      <path d="M62,22 H245 Q265,22 265,46 V78 H62 Z" fill="var(--tab)"/>
      <path d="M0,30 H62" stroke="var(--red)" stroke-width="5"/>
      <path d="M62,22 H245 Q265,22 265,48" fill="none" stroke="var(--red)" stroke-width="5"/>
      <path d="M542,22 H358 Q338,22 338,46 V78 H542 Z" fill="var(--tab)"/>
      <path d="M542,30 H600" stroke="var(--red)" stroke-width="5"/>
      <path d="M542,22 H358 Q338,22 338,48" fill="none" stroke="var(--red)" stroke-width="5"/>
      <path d="M531,708 H372 Q302,708 302,790 Q302,860 372,860 H531 Z" fill="#050505"/>
      <path d="M531,708 H372 Q302,708 302,790 Q302,860 372,860 H531" fill="none" stroke="url(#goldFade)" stroke-width="4"/>
      <path d="M531,714 H600" stroke="var(--gold)" stroke-width="4"/>
    </svg>

    <h2 class="section-title script" style="left:126px;top:26px">Pates</h2>
    <h2 class="section-title script" style="left:392px;top:26px">Supplements</h2>

    <h3 class="label script" style="left:22px;top:78px">Spaghetti :</h3>
    <ul class="menu" style="left:22px;top:104px;width:242px;--pc:30px">
      <li><span class="name">carbonnara</span><span class="price">14€</span></li>
      <li><span class="name">bolognaise</span><span class="price">14€</span></li>
      <li><span class="name">arabiata</span><span class="price">13€</span></li>
      <li><span class="name">Ati :</span><span class="price">18€</span></li>
      <li><span class="name">Saumon :</span><span class="price">17€</span></li>
    </ul>

    <h3 class="label script" style="left:22px;top:216px">Penne</h3>
    <ul class="menu" style="left:22px;top:242px;width:242px;--pc:30px">
      <li><span class="name">carbonara</span><span class="price">14€</span></li>
      <li><span class="name">bolognaise</span><span class="price">14€</span></li>
      <li><span class="name">arabiata</span><span class="price">13€</span></li>
      <li><span class="name">ati</span><span class="price">18€</span></li>
      <li><span class="name">saumon</span><span class="price">17€</span></li>
    </ul>

    <h3 class="label script" style="left:22px;top:354px">Tagliatelle</h3>
    <ul class="menu" style="left:22px;top:380px;width:242px;--pc:30px">
      <li><span class="name">carbonara</span><span class="price">14€</span></li>
      <li><span class="name">bolognaise</span><span class="price">14€</span></li>
      <li><span class="name">arabiata</span><span class="price">13€</span></li>
      <li><span class="name">ati</span><span class="price">18€</span></li>
      <li><span class="name">saumon</span><span class="price">17€</span></li>
    </ul>

    <h3 class="label script" style="left:313px;top:80px">fromages:</h3>
    <ul class="menu" style="left:316px;top:105px;width:136px;--pc:34px">
      <li><span class="name">mozza</span><span class="price">1,50€</span></li>
      <li><span class="name">burrata</span><span class="price">3,50€</span></li>
      <li><span class="name">buffala</span><span class="price">5€</span></li>
      <li><span class="name">chevre</span><span class="price">2€</span></li>
      <li><span class="name">st nectaire</span><span class="price">2,50€</span></li>
      <li><span class="name">gorgonzola</span><span class="price">2€</span></li>
      <li><span class="name">parmesan</span><span class="price">2,50€</span></li>
      <li><span class="name">ricotta</span><span class="price">2€</span></li>
    </ul>

    <h3 class="label script" style="left:316px;top:268px">Viandes</h3>
    <ul class="menu" style="left:316px;top:293px;width:100px;--pc:0px">
      <li><span class="name">poulet</span></li>
      <li><span class="name">viande hachee</span></li>
      <li><span class="name">merguez</span></li>
      <li><span class="name">jambon cuit</span></li>
      <li><span class="name">lardon</span></li>
      <li><span class="name">jambon de parme</span></li>
      <li><span class="name">thon</span></li>
      <li><span class="name">saumon</span></li>
      <li><span class="name">chorizo</span></li>
      <li><span class="name">fruit de mer</span></li>
      <li><span class="name">scampi</span></li>
      <li><span class="name">andouillette</span></li>
      <li><span class="name">jambon cru</span></li>
    </ul>
    <ul class="menu" style="left:418px;top:279px;width:34px;--pc:34px">
      <li><span></span><span class="price">2,50€</span></li>
      <li><span></span><span class="price">2,50€</span></li>
      <li><span></span><span class="price">2,50€</span></li>
      <li><span></span><span class="price">2€</span></li>
      <li><span></span><span class="price">2€</span></li>
      <li><span></span><span class="price">3,50€</span></li>
      <li><span></span><span class="price">2€</span></li>
      <li><span></span><span class="price">3,50€</span></li>
      <li><span></span><span class="price">2,50€</span></li>
      <li><span></span><span class="price">3,50€</span></li>
      <li><span></span><span class="price">3,50€</span></li>
      <li><span></span><span class="price">2€</span></li>
      <li><span></span><span class="price">2€</span></li>
    </ul>

    <h3 class="label script" style="left:462px;top:80px">Legumes</h3>
    <ul class="menu" style="left:462px;top:104px;width:138px;--pc:34px">
      <li><span class="name">poivron</span><span class="price">1,50€</span></li>
      <li><span class="name">champignon</span><span class="price">2€</span></li>
      <li><span class="name">oignon</span><span class="price">1,50€</span></li>
      <li><span class="name">pomme de terre</span><span class="price">2€</span></li>
      <li><span class="name">aubergine</span><span class="price">1,50€</span></li>
      <li><span class="name">artichaud</span><span class="price">2€</span></li>
      <li><span class="name">courgette</span><span class="price">2€</span></li>
      <li><span class="name">roquette</span><span class="price">2€</span></li>
      <li><span class="name">tomate cerise</span><span class="price">1,50€</span></li>
      <li><span class="name">capre</span><span class="price">1€</span></li>
      <li><span class="name">all</span><span class="price">1€</span></li>
      <li><span class="name">olive</span><span class="price">1,50€</span></li>
      <li><span class="name">anchois</span><span class="price">1€</span></li>
      <li><span class="name">ceuf</span><span class="price">2€</span></li>
      <li><span class="name">pistache</span><span class="price">1€</span></li>
    </ul>

    <h3 class="section-title script" style="left:22px;top:554px;font-size:36px">Salades</h3>
    <ul class="menu" style="left:22px;top:594px;width:233px;--pc:44px">
      <li><span><span class="name">Nicoise</span><span class="desc">tomate, thon,olive,pomme de terre</span></span><span class="price">15,50€</span></li>
      <li><span><span class="name">Norvegienne</span><span class="desc">tomate, saumon,oignon</span></span><span class="price" style="margin-left:2px">16€</span></li>
      <li><span><span class="name">Chevre chaud</span><span class="desc">tomate lardon, chevre sur toast</span></span><span class="price" style="margin-left:2px">16€</span></li>
      <li><span><span class="name">Jambon</span><span class="desc">jambon, roquette, parmesan</span></span><span class="price" style="margin-left:2px">16€</span></li>
    </ul>

    <h3 class="section-title script" style="left:16px;top:682px;font-size:38px">Desserts</h3>
    <div class="desserts abs" style="left:22px;top:720px">
      <p>Mousse au chocolat<span class="price">7€</span></p>
      <p>Tiramisu: classique, choco<span class="price" style="margin-left:10px">7€</span></p>
      <p>Baba au rhum<span class="price" style="margin-left:24px">8€</span></p>
      <p>Crème brulè<span class="price" style="margin-left:24px">6,50€</span></p>
      <p>Café : expresso 1,80€<span class="price" style="margin-left:20px">Thé : 1,50€</span></p>
      <p>capuccino : 2,20€</p>
    </div>

    <p class="drink-head" style="top:569px"><span class="script">Boissons</span><span class="bold" style="margin-left:-6px">33cl</span><span class="bold" style="margin-left:14px">2,50€</span></p>
    <p class="drinks" style="top:590px;width:190px">Kola, kola zero, kola cherry, fizzy, limo sunjus, eau,teafresh,fruity, fruity pomme cassis</p>
    <p class="drink-head" style="top:633px"><span class="script">Boissons bouteille</span><span class="bold" style="margin-left:10px">5,50 €</span></p>
    <p class="drinks" style="top:654px">kola, fizzy, aqua frizzante ,teafresh</p>
    <p class="drink-head" style="top:669px"><span class="script">Alcools et vin</span></p>

    <h2 class="programme-title script">Programme</h2>
  </section>

</main>
</body>
</html>
```